Business card design needed

I would like a clean simple buisness card as a freelance makeup artist.The main colours i would like are black, white card (grey tones) with a pop of red or purple. Card mostly white. Double sided. Front side featuring a vector graphic plain face chart-similiar to the KIV/Fabrizio Lentard design. Face can be partially shown/cropped or in full. Some white space near text at the front - "Dorit Pell MUA" then in smaller text underneath "Make me over" then rest of the contact details.Font is walkway font.

Business

Dorit Pell MUA Make me over m: 0437 182 906 e: dorita_pell@quillpost.net

```html
<!DOCTYPE html>
<html lang="en">
<head>
<meta charset="utf-8">
<title>Dorit Pell MUA – Business Card</title>
<link rel="stylesheet" href="https://fonts.googleapis.com/css2?family=Questrial&display=swap">
<style>
  :root {
    --backdrop: #ebeceb;
    --card: #ffffff;
    --ink: #1e1e1e;
    --accent-red: #e0141e;
    --hair-dark: #262626;
    --hair-grey: #9a9a9a;
    --shadow: rgba(0, 0, 0, 0.22);
  }
  * { margin: 0; padding: 0; box-sizing: border-box; }
  html, body {
    width: 1200px;
    height: 476px;
    overflow: hidden;
    background: var(--backdrop);
    font-family: "Questrial", sans-serif;
    color: var(--ink);
  }
  .canvas { position: relative; width: 1200px; height: 476px; }

  .card {
    position: absolute;
    top: 90px;
    width: 527px;
    height: 292px;
    background: var(--card);
    border-radius: 18px;
    overflow: hidden;
    box-shadow: 3px 6px 10px var(--shadow);
  }
  .card--front { left: 55px; }
  .card--back  { left: 628px; }

  .face-art {
    position: absolute;
    top: 0;
    height: 100%;
  }
  .card--front .face-art {
    left: 0;
    width: 150px;
    background: linear-gradient(90deg, var(--hair-dark) 0%, var(--hair-dark) 40%, #f4f4f4 100%);
  }
  .card--back .face-art {
    right: 0;
    width: 135px;
    background: linear-gradient(270deg, var(--hair-grey) 0%, var(--hair-grey) 30%, #f6f6f6 100%);
  }

  .brand-name {
    position: absolute;
    color: var(--accent-red);
    white-space: nowrap;
    letter-spacing: 0.5px;
  }
  .tagline {
    position: absolute;
    color: var(--ink);
    white-space: nowrap;
  }
  .card--front .brand-name { left: 217px; top: 110px; font-size: 29px; }
  .card--front .tagline    { left: 256px; top: 157px; font-size: 18px; }
  .card--back .brand-name  { left: 99px;  top: 74px;  font-size: 24px; }
  .card--back .tagline     { left: 103px; top: 104px; font-size: 15px; }

  .contact-list {
    position: absolute;
    left: 78px;
    top: 143px;
    list-style: none;
  }
  .contact-item {
    display: flex;
    align-items: center;
    height: 28px;
    font-size: 20px;
    white-space: nowrap;
  }
  .contact-icon {
    width: 16px;
    height: 16px;
    margin-right: 9px;
    flex: none;
  }
</style>
</head>
<body>
<div class="canvas">

  <section class="card card--front">
    <div class="face-art" role="img" aria-label="Line illustration of a woman's face framed by dark flowing hair"></div>
    <h1 class="brand-name">Dorit Pell MUA</h1>
    <p class="tagline">Make me over</p>
  </section>

  <section class="card card--back">
    <h2 class="brand-name">Dorit Pell MUA</h2>
    <p class="tagline">Make me over</p>
    <ul class="contact-list">
      <li class="contact-item">
        <svg class="contact-icon" viewBox="0 0 16 16" aria-hidden="true">
          <rect x="4" y="1" width="8" height="14" rx="1.5" fill="none" stroke="var(--accent-red)" stroke-width="1.4"/>
          <line x1="4" y1="11.5" x2="12" y2="11.5" stroke="var(--accent-red)" stroke-width="1.2"/>
        </svg>
        <span>0437 182 906</span>
      </li>
      <li class="contact-item">
        <svg class="contact-icon" viewBox="0 0 16 16" aria-hidden="true">
          <rect x="1" y="3.5" width="14" height="9" fill="none" stroke="var(--accent-red)" stroke-width="1.3"/>
          <polyline points="1,3.5 8,9 15,3.5" fill="none" stroke="var(--accent-red)" stroke-width="1.3"/>
        </svg>
        <span>dorita_pell@quillpost.net</span>
      </li>
    </ul>
    <div class="face-art" role="img" aria-label="Soft grey line illustration of a woman's face framed by flowing hair"></div>
  </section>

</div>
</body>
</html>
```